2-Page Flyer for the Information Session about the Tranquil Venture Course

This is a flyer to announce/advertise an evening Information Session about the Tranquil Venture Course. This Program aims at mindfully rethinking and redesigning work (and life) for people who feel stuck or not entirely satisfied with their work and/or life (please see draft flyer attached for more details). This Program is property of Brightfold Joy, a company that uses a combination of Mindfulness, Design, and Entrepreneurship to help people achieve greater happiness (in their work and lives).
Updates

Target Market(s)

People who feel stuck or not entirely satisfied with their work and/or life (please see draft flyer attached for more details)

Font styles to use
Serif
Sans Serif

Colors
ffffff
f37122
33a6d7
acd037

Requirements
Must have
• All of what I will say below is suggestive (I’m not a design expert), and I’m open to divert from it, if it makes sense and feels more interesting.
• I thought initially of a 2-page flyer (please see draft flyer attached). The first page could help people grasp the essence of the event quickly (in 1 or 2 minutes), and then, if they are interested/motivated, they would continue reading through page 2, which has more info about the Program in itself.
• Potential Structure
• Page 1
• . About the Information Session on the Tranquil Venture Course
• . Visible Date & Time, Contacts, Venue (and other relevant info)
• . About me (the facilitator)
• Page 2
• . About the Tranquil Venture Course
• I include a Powerpoint draft of the flyer with the content. The design is rudimentary and precarious from an aesthetics/organization point of view, and this is mainly where I need help (and maybe in other aspects too!).
• On the flyer, I would like to include:
• . A photo of myself (I attach 1 picture).
• . 1 or 2 beautiful-nature photos (cropped or full). One may have to do with looking at the sky, dreaming, and imagining a new work and life (2 photos with sky and clouds attached). The other has to do with walking the transformation journey (the photo with the person walking through the forest path).
• . brightfold joy logo or logos (there are two slightly different ones, that can be used for different purposes). For the first page, I would like the brightfold joy logo that has "brightfold joy" written on the bottom, with the saying "Stillness, Craft and Venture for Joy" beneath. This is the main logo. For the 2nd page, you can choose the logo that adapts better.
• - Where it says the "the way out is in" it would be great to have a similar font to the one I attach (see file "Font_the_way_out_is_in.png" and Ankecallig-fg.ttf
Nice to have
• In terms of colours, I would not divert much from the logo colours (and of course white and black). I would like the flyer to be quite white. Almost like fairy-tale white: the white horse, the white snow, the white of the stars, the white heaven. White could be the base colour. White means peace, tranquillity, calm contentment, a smile.
• And then use the other colours. The green of the mindfulness. The blue of the sky, the dreams. And the orange of the sun, the energy, the fire, the action. And maybe the black for text.
• Where it says the "the way out is in" it would be great to have a similar font to the one I attach (see file "Font_the_way_out_is_in".
• I would like this flyer to be a piece of art, in every possible way. Simple, beautiful, ease, light, peaceful, calm happy. Just like the Tranquil Venture Course and brightfold joy Company that I am creating intends to be. The mission of this Program and Company is to be a designer, a painter (a Picasso) of happier and more fulfilling human lives.
• I am very much looking forward to seeing your proposal(s).

```html
<!DOCTYPE html>
<html lang="en">
<head>
<meta charset="utf-8">
<title>Tranquil Venture Course – Information Session</title>
<link href="https://fonts.googleapis.com/css2?family=Cinzel:wght@600;700&family=Oswald:wght@600&family=Roboto+Condensed:ital,wght@0,400;0,700;1,400&family=Tinos:ital@1&display=swap" rel="stylesheet">
<style>
  :root {
    --white: #ffffff;
    --orange: #f37122;
    --blue: #33a6d7;
    --green: #acd037;
    --ink: #111111;
    --black: #000000;
  }
  html, body { margin: 0; padding: 0; overflow: hidden; background: var(--white); }
  .flyer {
    position: relative; width: 849px; height: 1200px; overflow: hidden;
    background: var(--white); color: var(--ink);
    font-family: "Roboto Condensed", "Arial Narrow", sans-serif;
  }
  .decor { position: absolute; inset: 0; }
  .hero-photo {
    position: absolute; left: -2px; top: -48px; width: 346px; height: 346px; border-radius: 50%;
    background: radial-gradient(circle at 40% 55%, #e9e4da 0%, #b9b39f 30%, #4f6a55 65%, #2f4a3c 100%);
  }
  .brand { position: absolute; left: 560px; top: 30px; width: 272px; text-align: center; }
  .brand-dot { width: 64px; height: 64px; border-radius: 50%; background: var(--orange); margin: 0 auto 10px; }
  .brand-name { font-size: 26px; font-weight: 400; color: var(--blue); line-height: 1; letter-spacing: 0.2px; }
  .brand-tagline { font-size: 14px; font-style: italic; color: var(--ink); margin-top: 6px; }
  .session-pill {
    position: absolute; left: 419px; top: 194px; width: 377px; height: 57px; border-radius: 29px;
    background: var(--orange); color: var(--white); box-shadow: 2px 3px 4px rgba(0,0,0,.2);
    font-family: "Cinzel", Georgia, serif; font-weight: 700; font-size: 25px;
    display: flex; align-items: center; justify-content: center; letter-spacing: 1px;
  }
  .event-when {
    position: absolute; left: 380px; top: 258px; width: 455px; text-align: center;
    font-family: "Cinzel", Georgia, serif; font-weight: 700; color: var(--blue);
    font-size: 25px; line-height: 28px;
  }
  .program-title {
    position: absolute; left: 0; top: 342px; width: 889px; text-align: center;
    font-family: "Oswald", "Arial Narrow", sans-serif; font-weight: 600; font-variant: small-caps;
    color: var(--orange); font-size: 56px; line-height: 1; letter-spacing: 0.5px;
  }
  .section { position: absolute; left: 81px; width: 700px; }
  .section h2 {
    margin: 0 0 6px; font-family: "Cinzel", Georgia, serif; font-weight: 700;
    color: var(--blue); font-size: 25px; letter-spacing: 1px; line-height: 1;
  }
  .section p { margin: 0; font-weight: 700; font-size: 15px; line-height: 24px; }
  .hl { color: var(--orange); }
  .section-info { top: 456px; }
  .section-who { top: 558px; }
  .facilitator-photo {
    position: absolute; left: 0; top: 681px; width: 295px; height: 468px;
    background: linear-gradient(180deg, #ffffff 0%, #f2f2f2 30%, #3d5468 60%, #2b3d4d 100%);
  }
  .facilitator-pill {
    position: absolute; left: 436px; top: 731px; width: 244px; height: 34px;
    border: 3px solid var(--blue); border-radius: 20px;
    display: flex; align-items: center; justify-content: center;
    font-family: "Cinzel", Georgia, serif; font-weight: 700; color: var(--blue); font-size: 25px;
  }
  .facilitator-name {
    position: absolute; left: 330px; top: 784px; width: 460px; text-align: center;
    font-family: "Cinzel", Georgia, serif; font-weight: 700; color: var(--blue); font-size: 35px; line-height: 1;
  }
  .facilitator-role {
    position: absolute; left: 330px; top: 826px; width: 460px; text-align: center;
    font-family: "Cinzel", Georgia, serif; font-weight: 700; color: var(--blue); font-size: 15.5px;
  }
  .bio { position: absolute; left: 343px; top: 863px; width: 435px; }
  .bio p {
    margin: 0 0 17px; font-family: "Tinos", "Times New Roman", serif; font-style: italic;
    font-size: 13px; line-height: 17.2px; text-align: justify;
  }
  .more-link { position: absolute; left: 343px; top: 1115px; font-weight: 700; font-size: 15px; }
  .more-link span { color: var(--blue); }
  .booking {
    position: absolute; left: 0; top: 1149px; width: 849px; height: 51px; background: var(--black);
    color: var(--white); text-align: center; font-weight: 700;
  }
  .booking h3 { margin: 2px 0 0; font-size: 20px; line-height: 24px; font-weight: 700; }
  .booking-details { font-size: 13.5px; line-height: 20px; white-space: nowrap; }
  .booking-details .value { color: var(--blue); }
  .booking-details .gap { display: inline-block; width: 16px; }
</style>
</head>
<body>
<div class="flyer">
  <svg class="decor" width="849" height="1200" viewBox="0 0 849 1200" aria-hidden="true">
    <path d="M330 0 L849 0 L849 8 C700 30 500 70 345 112 Z" fill="var(--green)"/>
    <circle cx="172" cy="128" r="183" fill="var(--green)"/>
    <path d="M0 240 L0 505 C20 420 50 350 100 300 L60 290 Z" fill="var(--green)"/>
  </svg>

  <div class="hero-photo" role="img" aria-label="Photo of a woman in a hat resting by a wooden post, eyes closed, facing the sky"></div>

  <div class="brand">
    <div class="brand-dot"></div>
    <div class="brand-name">brightfold joy</div>
    <div class="brand-tagline">Stillness, Craft and Venture for Joy</div>
  </div>

  <div class="session-pill">INFORMATION SESSION</div>
  <div class="event-when">Thursday 5th September 2019<br>19:30 to 21:00</div>

  <h1 class="program-title">Tranquil Venture Course</h1>

  <section class="section section-info">
    <h2>INFORMATION SESSION</h2>
    <p>The purpose of this <span class="hl">Information Session</span> is to give you a real insight into the <span class="hl">Tranquil Venture Course</span> and how it can help you make the most of your professional and personal life.</p>
  </section>

  <section class="section section-who">
    <h2>WHO CAN COME</h2>
    <p>The Information Session is <span class="hl">FREE</span>. Whether you come on your own, or with friends or family, you’ll be warmly welcome. It will take place on <span class="hl">Thursday the 5th September 2019, from 19:30 to 21:00</span>, at <span class="hl">Kelpie Coworking.</span><br>Please get in touch for more info or to book a place.</p>
  </section>

  <div class="facilitator-photo" role="img" aria-label="Portrait photo of the facilitator in a blue jacket and scarf"></div>

  <div class="facilitator-pill">FACILITATOR</div>
  <div class="facilitator-name">Dr Tomas Avelar</div>
  <div class="facilitator-role">Visiting Research Fellow, University of Wexmoor</div>

  <div class="bio">
    <p>Tomas joined the University of Wexmoor (School of Management) as a Lecturer in Entrepreneurship in 2015. He completed his PhD in Entrepreneurship at Calderbrook Business School in 2014.</p>
    <p>His work received the Lanfield Doctoral Dissertation Award from the Society for Venture Studies. He began his business career as a production engineer (Voltrane), and continued in sales (Kessler Industrial). After his MBA, he worked as a strategy consultant at Douro Business School.</p>
    <p>Originally from Portugal, Tomas enjoys designing and launching new ideas, international communities, mindfulness retreats, and musical improvisation. He nurtures a close connection to Quiet Meadow Mindfulness Centre, where he has practiced and volunteered over 9 months. He has a broad experience of sharing the benefits of mindfulness with others.</p>
  </div>

  <div class="more-link">More about the facilitator: <span>www.profiles.example/tomasavelar</span></div>

  <footer class="booking">
    <h3>Information &amp; Booking</h3>
    <div class="booking-details">Email: <span class="value">info@brightfoldjoy.example</span><span class="gap"></span>Tel: <span class="value">+34 600 000 123 (video call and messaging)</span><span class="gap"></span>Venue: <span class="value">Kelpie Coworking, C/ Alzina 42, Barcelona</span></div>
  </footer>
</div>
</body>
</html>
```